Providing Back Office Solutions to Financial Advisors and Attorney Needs a Business Card Design

Need a Business Card Design that speaks to Financial Advisor and Attorneys. Some of the word that come to mind is Clean/Simple & Futuristic.

Industry/Entity Type

Business

```html
<!DOCTYPE html>
<html lang="en">
<head>
<meta charset="utf-8">
<title>Korvant Back Office Solutions — Business Card</title>
<link rel="stylesheet" href="https://fonts.googleapis.com/css2?family=Source+Sans+3:wght@400;600;700&display=swap">
<style>
  :root {
    --brand-blue: #1a62ad;
    --brand-blue-dark: #0f4f95;
    --card-white: #ffffff;
    --ink: #1f2328;
    --backdrop: #e9ecef;
    --card-shadow: rgba(20, 30, 45, 0.18);
  }
  * { box-sizing: border-box; margin: 0; padding: 0; }
  html, body {
    width: 1200px; height: 800px; overflow: hidden;
    background: var(--backdrop);
    font-family: "Source Sans 3", "Myriad Pro", Arial, sans-serif;
    color: var(--ink);
  }
  .stage {
    position: relative; width: 1200px; height: 800px;
    display: flex; align-items: center; justify-content: center; gap: 40px;
  }
  .card {
    position: relative; width: 540px; height: 309px;
    background: var(--card-white);
    box-shadow: 0 6px 18px var(--card-shadow);
    overflow: hidden;
  }

  /* Brand lockup: plain circle + divider + name */
  .brand { display: flex; align-items: center; }
  .brand-dot { border-radius: 50%; background: var(--brand-blue); flex: none; }
  .brand-rule { width: 1.5px; background: var(--brand-blue-dark); margin: 0 12px; flex: none; }
  .brand-name {
    color: var(--brand-blue); font-weight: 600; text-transform: uppercase;
    line-height: 1.05; letter-spacing: 0.04em;
  }
  .brand-name .line-main { display: block; }
  .brand-name .line-sub { display: block; }

  /* Front */
  .card-front .brand { position: absolute; left: 50%; top: 50%; transform: translate(-50%, -50%); }
  .card-front .brand-dot { width: 66px; height: 66px; }
  .card-front .brand-rule { height: 76px; }
  .card-front .line-main { font-size: 40px; }
  .card-front .line-sub { font-size: 15.5px; }

  /* Back */
  .card-back .brand { position: absolute; left: 28px; top: 46px; }
  .card-back .brand-dot { width: 58px; height: 58px; }
  .card-back .brand-rule { height: 68px; }
  .card-back .line-main { font-size: 35px; }
  .card-back .line-sub { font-size: 13.5px; }

  .title-ribbon { position: absolute; left: 380px; top: 0; width: 150px; height: 170px; }
  .title-ribbon svg { position: absolute; inset: 0; }
  .title-ribbon .holder {
    position: absolute; left: 0; right: 0; top: 44px;
    text-align: center; color: var(--card-white); line-height: 1.05;
  }
  .holder-name { font-size: 17px; font-weight: 700; letter-spacing: 0.02em; }
  .holder-role { font-size: 16px; font-weight: 400; }

  .corner-dot {
    position: absolute; left: 409px; top: 192px; width: 92px; height: 92px;
    border-radius: 50%; background: var(--brand-blue);
  }

  .contact-list { position: absolute; left: 40px; top: 186px; list-style: none; }
  .contact-list li { display: flex; align-items: center; font-size: 15.5px; height: 22px; }
  .contact-list svg { width: 13px; height: 13px; margin-right: 10px; flex: none; }
  .contact-list .site-alt { padding-left: 23px; }
</style>
</head>
<body>
<main class="stage">
  <section class="card card-front" aria-label="Card front">
    <div class="brand">
      <span class="brand-dot"></span>
      <span class="brand-rule"></span>
      <span class="brand-name"><span class="line-main">Korvant</span><span class="line-sub">Back Office Solutions</span></span>
    </div>
  </section>

  <section class="card card-back" aria-label="Card back">
    <div class="brand">
      <span class="brand-dot"></span>
      <span class="brand-rule"></span>
      <span class="brand-name"><span class="line-main">Korvant</span><span class="line-sub">Back Office Solutions</span></span>
    </div>

    <div class="title-ribbon">
      <svg viewBox="0 0 150 170" width="150" height="170" aria-hidden="true">
        <polygon points="0,0 150,0 150,128 75,170 0,128" fill="var(--brand-blue-dark)"/>
      </svg>
      <div class="holder">
        <div class="holder-name">JOHN DOE</div>
        <div class="holder-role">manager</div>
      </div>
    </div>

    <span class="corner-dot"></span>

    <ul class="contact-list">
      <li>
        <svg viewBox="0 0 16 16" aria-hidden="true"><path d="M4 1.5l2.2 2.8-1.4 1.6c.8 1.9 2.3 3.4 4.2 4.2l1.6-1.4 2.8 2.2-1.5 2.6C7 13 3 9 1.5 3z" fill="var(--brand-blue)"/></svg>
        012 345 6789
      </li>
      <li>
        <svg viewBox="0 0 16 16" aria-hidden="true"><rect x="1.5" y="3.5" width="13" height="9" fill="none" stroke="var(--brand-blue)" stroke-width="1.5"/><path d="M1.5 3.5L8 9l6.5-5.5" fill="none" stroke="var(--brand-blue)" stroke-width="1.5"/></svg>
        email@korvantbackoffice.com
      </li>
      <li>
        <svg viewBox="0 0 16 16" aria-hidden="true"><circle cx="8" cy="8" r="6.5" fill="none" stroke="var(--brand-blue)" stroke-width="1.4"/><ellipse cx="8" cy="8" rx="2.8" ry="6.5" fill="none" stroke="var(--brand-blue)" stroke-width="1.2"/><path d="M1.5 8h13" stroke="var(--brand-blue)" stroke-width="1.2"/></svg>
        www.korvantbackoffice.com
      </li>
      <li class="site-alt">www.korvantbackofficesolutions.com</li>
    </ul>
  </section>
</main>
</body>
</html>
```